Larkspur Elementary
Stationary, Letterhead, Business Card
Simple
Cora P. Wendt
Counselor
742 Ridgeway Lane
Brindlewood, XX 40917
wendt_cora@mbxsd.org
http://les.hollowmere.k12.xx.us
I would like to stay with the navy gold and blue theme (but variations are fine) but a white background is not necessary.
I like the vertical look more than the horizontal but both are welcomed.
If you follow the link, I like how #8, #15, and #18 look format-wise.
I look forward to your designs.
http://www.quarvelblog.com/2008/06/25/yet-another-post-with-unique-business-cards/
Logo plus your creative touches

```html
<!DOCTYPE html>
<html lang="en">
<head>
<meta charset="utf-8">
<title>Larkspur Elementary Counseling – Stationery</title>
<link href="https://fonts.googleapis.com/css2?family=Open+Sans:ital,wght@0,400;0,600;0,800;1,400&display=swap" rel="stylesheet">
<style>
  :root{
    --navy:#1f2a6b;
    --gold:#e3a82b;
    --blue:#2a8fd0;
    --ink:#3a3a3a;
    --muted:#6a6a6a;
    --paper:#ffffff;
    --backdrop:#d9dadb;
  }
  *{box-sizing:border-box;margin:0;padding:0}
  html,body{width:1200px;height:840px;overflow:hidden}
  body{background:var(--backdrop);font-family:"Open Sans",Arial,sans-serif;color:var(--ink);position:relative}

  .sheet{position:absolute;background:var(--paper);box-shadow:0 1px 4px rgba(0,0,0,.18);overflow:hidden}

  /* brand mark */
  .brand{display:flex;align-items:center;gap:6px}
  .brand-square{width:14px;height:14px;background:var(--gold);flex:none}
  .brand-name{font-weight:800;color:var(--navy);line-height:1.05;text-transform:uppercase;font-size:15px;letter-spacing:.3px}
  .brand-name span{display:block;font-size:8.5px;letter-spacing:.6px}

  /* contact block */
  .contact{font-size:6.5px;line-height:9px;color:var(--ink);font-style:normal}
  .contact dl{display:grid;grid-template-columns:26px auto;margin-top:4px}
  .contact dt{color:var(--blue);font-weight:600}

  /* footer stripe */
  .stripe{position:absolute;left:0;right:0;background:var(--navy);border-top:2px solid var(--gold);box-shadow:0 3px 0 var(--blue)}
  .stripe-url{color:#fff;font-size:7px;font-weight:600;position:absolute;left:24px;top:50%;transform:translateY(-50%)}

  /* letterhead */
  .letterhead{left:29px;top:24px;width:440px;height:792px}
  .letterhead .brand{position:absolute;left:26px;top:30px}
  .letterhead .contact{position:absolute;left:300px;top:28px}
  .letter-body{position:absolute;left:26px;top:112px;width:380px;font-size:6.6px;line-height:9.4px;color:var(--ink)}
  .letter-body p{margin-bottom:9px}
  .letter-body .cite{font-style:italic;color:var(--muted)}
  .letter-body .sign{margin-top:24px}
  .letterhead .stripe{bottom:36px;height:26px}

  /* envelope */
  .envelope{left:492px;top:60px;width:684px;height:384px}
  .envelope .brand{position:absolute;left:26px;top:24px}
  .envelope .brand-name{font-size:19px}
  .envelope .brand-name span{font-size:10px}
  .envelope .return{position:absolute;left:26px;top:78px;font-size:7px;line-height:10px}
  .envelope .stripe{bottom:30px;height:14px}

  /* business cards */
  .card{width:300px;height:172px}
  .card-front{left:504px;top:480px}
  .card-front .brand{position:absolute;left:16px;top:18px}
  .card-front .brand-name{font-size:13px}
  .card-front .brand-name span{font-size:7px}
  .card-front .contact{position:absolute;left:16px;top:70px}
  .card-front .person{position:absolute;right:14px;top:74px;text-align:right}
  .person-name{display:inline-block;background:var(--navy);color:#fff;font-size:8.5px;font-weight:800;letter-spacing:.6px;padding:3px 8px;text-transform:uppercase}
  .person-role{display:block;font-size:7px;color:var(--blue);font-weight:600;margin-top:3px}
  .card-front .stripe{bottom:14px;height:12px}

  .card-back{left:852px;top:600px}
  .card-back .stripe{bottom:22px;height:28px}
  .card-back .stripe-url{font-size:8px;left:auto;right:20px}
</style>
</head>
<body>

<section class="sheet letterhead" aria-label="Letterhead">
  <div class="brand">
    <div class="brand-square"></div>
    <div class="brand-name">Larkspur<span>Elementary Counseling</span></div>
  </div>
  <address class="contact">
    742 Ridgeway Lane<br>Brindlewood, XX 40917
    <dl>
      <dt>Phone</dt><dd>303.555.0142</dd>
      <dt>Fax</dt><dd>303.555.0143</dd>
      <dt>Email</dt><dd>wendt_cora@mbxsd.org</dd>
    </dl>
  </address>
  <div class="letter-body">
    <p>Dear,</p>
    <p>Someone / Somebody,</p>
    <p>"Our counseling team supports every student through friendly guidance, small group sessions and classroom lessons that build kindness, focus and confidence. We partner with families and teachers so each child feels safe, heard and ready to learn every single day."<br><span class="cite">Section 1.10.32 of "de Finibus Bonorum et Malorum", written by Tullian Vance in 45 BC</span></p>
    <p>"This year we are adding lunch bunch groups, a peer helper program and a family night each season. Please reach out with questions, ideas or concerns at any time; our door is always open and we are happy to meet."<br><span class="cite">1914 translation by H. Ardley</span></p>
    <p>"Thank you for helping our students grow in heart and mind. Together we can make our school a place where every learner belongs, tries new things and treats others with care."<br><span class="cite">Section 1.10.33 of "de Finibus Bonorum et Malorum", written by Tullian Vance in 45 BC</span></p>
    <p>Peace Today,<br>1914 translation by</p>
    <p class="sign">H. Ardley</p>
  </div>
  <div class="stripe"><span class="stripe-url">http://les.hollowmere.k12.xx.us</span></div>
</section>

<section class="sheet envelope" aria-label="Envelope">
  <div class="brand">
    <div class="brand-square"></div>
    <div class="brand-name">Larkspur<span>Elementary Counseling</span></div>
  </div>
  <address class="return contact">742 Ridgeway Lane<br>Brindlewood, XX 40917</address>
  <div class="stripe"></div>
</section>

<section class="sheet card card-front" aria-label="Business card front">
  <div class="brand">
    <div class="brand-square"></div>
    <div class="brand-name">Larkspur<span>Elementary Counseling</span></div>
  </div>
  <address class="contact">
    742 Ridgeway Lane<br>Brindlewood, XX 40917
    <dl>
      <dt>Phone</dt><dd>303.555.0142</dd>
      <dt>Fax</dt><dd>303.555.0143</dd>
      <dt>Email</dt><dd>wendt_cora@mbxsd.org</dd>
    </dl>
  </address>
  <div class="person">
    <span class="person-name">Cora P. Wendt</span>
    <span class="person-role">Counselor</span>
  </div>
  <div class="stripe"></div>
</section>

<section class="sheet card card-back" aria-label="Business card back">
  <div class="stripe"><span class="stripe-url">http://les.hollowmere.k12.xx.us</span></div>
</section>

</body>
</html>
```